Ray's Personal Training -> also needs a logo

Services Frankston, Mornington, and Somerville

Specializes in in-home personal training

VimTrek style workouts

Not really preferential colors but needs to look modern and not stock photo

Industry/Entity Type

Training

Requirements
Must have
• 30% off first time customers on a package of 10

```html
<!DOCTYPE html>
<html lang="en">
<head>
<meta charset="utf-8">
<title>Ray's Personal Training</title>
<link rel="stylesheet" href="https://fonts.googleapis.com/css2?family=Jost:wght@300;400;500;700;800&display=swap">
<style>
  :root {
    --navy: #1b1a5e;
    --sky: #7cc0f2;
    --teal: #3fd6c8;
    --blue: #2a2fd8;
    --violet: #7b22d6;
    --magenta: #c21a9a;
    --crimson: #d8173f;
    --white: #ffffff;
    --offer-panel: rgba(30, 26, 44, 0.88);
    --offer-text: #e9e9ee;
  }
  * { margin: 0; padding: 0; box-sizing: border-box; }
  html, body { width: 1200px; height: 900px; overflow: hidden; background: #111; }
  .poster {
    position: relative;
    width: 1200px;
    height: 900px;
    overflow: hidden;
    font-family: "Jost", "Futura", sans-serif;
    background:
      radial-gradient(ellipse 520px 380px at 0% 78%, var(--teal) 0%, rgba(63,214,200,0) 100%),
      radial-gradient(ellipse 520px 420px at 100% 0%, var(--crimson) 0%, rgba(216,23,63,0) 100%),
      linear-gradient(120deg, #2f5fe0 0%, var(--blue) 38%, var(--violet) 68%, var(--magenta) 100%);
  }
  .light-streaks {
    position: absolute;
    left: 0; top: 240px;
    width: 1200px; height: 480px;
    background:
      radial-gradient(ellipse 620px 120px at 45% 55%, rgba(255,255,255,0.75) 0%, rgba(230,220,255,0.35) 45%, rgba(255,255,255,0) 100%),
      radial-gradient(ellipse 420px 90px at 85% 35%, rgba(255,235,255,0.55) 0%, rgba(255,255,255,0) 100%);
  }
  .athlete-photo {
    position: absolute;
    left: 640px; top: 60px;
    width: 520px; height: 840px;
    border-radius: 40% 40% 0 0;
    background: radial-gradient(ellipse at 50% 35%, rgba(160,70,200,0.55) 0%, rgba(120,40,190,0.25) 55%, rgba(120,40,190,0) 100%);
  }
  .brand-name { text-transform: uppercase; }
  .brand-main {
    position: absolute;
    left: 40px; top: 42px;
    font-size: 240px;
    line-height: 1;
    font-weight: 500;
    letter-spacing: 6px;
    color: var(--navy);
    white-space: nowrap;
  }
  .brand-sub {
    position: absolute;
    left: 45px; top: 259px;
    font-size: 54px;
    line-height: 1;
    font-weight: 700;
    letter-spacing: 1px;
    color: var(--sky);
    white-space: nowrap;
  }
  .service-areas {
    position: absolute;
    left: 45px; top: 328px;
    color: var(--navy);
    text-transform: uppercase;
  }
  .service-areas h2 { font-size: 40px; line-height: 40px; font-weight: 800; }
  .service-areas li { list-style: none; font-size: 33px; line-height: 34px; font-weight: 400; }
  .specialties {
    position: absolute;
    left: 45px; top: 726px;
    color: var(--white);
    text-transform: uppercase;
    line-height: 1.02;
  }
  .specialties h2 { font-size: 48px; font-weight: 800; }
  .specialties li { list-style: none; font-size: 51px; font-weight: 300; letter-spacing: 0.5px; }
  .offer-panel { position: absolute; left: 0; top: 0; }
  .offer {
    position: absolute;
    right: 34px; top: 622px;
    width: 320px;
    text-align: right;
    color: var(--offer-text);
  }
  .offer .offer-amount { font-size: 88px; font-weight: 300; line-height: 0.9; }
  .offer .offer-rule { height: 2px; background: var(--offer-text); margin: 12px 0 10px; }
  .offer .offer-terms { font-size: 27px; font-weight: 700; line-height: 1.25; }
</style>
</head>
<body>
  <main class="poster">
    <div class="light-streaks" role="img" aria-label="Abstract white and violet light streaks sweeping across the background"></div>
    <div class="athlete-photo" role="img" aria-label="Photo of a woman lifting dumbbells, tinted purple"></div>

    <h1 class="brand-name">
      <span class="brand-main">Rays</span>
      <span class="brand-sub">Personal Training</span>
    </h1>

    <section class="service-areas">
      <h2>Services:</h2>
      <ul>
        <li>Frankston</li>
        <li>Mornington</li>
        <li>Somerville</li>
      </ul>
    </section>

    <section class="specialties">
      <h2>Specializes in:</h2>
      <ul>
        <li>In-home personal training</li>
        <li>VimTrek style workouts</li>
      </ul>
    </section>

    <svg class="offer-panel" width="1200" height="900" viewBox="0 0 1200 900" aria-hidden="true">
      <polygon points="700,900 1200,438 1200,900" fill="var(--offer-panel)"/>
    </svg>

    <section class="offer">
      <div class="offer-amount">30%<br>OFF</div>
      <div class="offer-rule"></div>
      <p class="offer-terms">first time customers<br>on a package of 10</p>
    </section>
  </main>
</body>
</html>
```